TRV business card

Need a business card for a company that provides instructional design and elearning development services. The website is here: http://tarvexa.studio/

I'm attaching a current logo, as well as the old business card design. While I like to keep it clean, the old design is too simplistic for my liking. The only idea I want to reuse from the old design is placing industry jargon on the back of the card, just need a better way to present it. But if you have other ideas for the back--feel free to experiment.

Please use the colors complementary to the color we have on the website. Thank you!

```html
<!DOCTYPE html>
<html lang="en">
<head>
<meta charset="utf-8">
<title>TRV business card</title>
<link rel="stylesheet" href="https://fonts.googleapis.com/css2?family=Open+Sans:wdth,wght@75..100,400..800&display=swap">
<style>
  :root {
    --teal: #17b3ae;
    --gold: #d8cc92;
    --ink: #2b2b2b;
    --rule: #3a3a3a;
    --paper: #ffffff;
    --backdrop: #e6e6e6;
  }
  * { margin: 0; padding: 0; box-sizing: border-box; }
  html, body { width: 1200px; height: 1200px; overflow: hidden; }
  body {
    background: var(--backdrop);
    font-family: "Open Sans", Arial, sans-serif;
    position: relative;
  }
  .card {
    position: absolute;
    left: 150px;
    width: 900px;
    height: 514px;
    box-shadow: 0 6px 18px rgba(0,0,0,0.18);
    overflow: hidden;
  }
  .card--front { top: 56px; background: var(--paper); }
  .card--back { top: 630px; background: var(--teal); }

  .brand {
    position: absolute;
    left: 42px;
    top: 66px;
    display: flex;
    align-items: center;
    gap: 22px;
  }
  .brand__mark {
    width: 62px;
    height: 62px;
    background: var(--teal);
  }
  .brand__name {
    font-size: 78px;
    font-weight: 700;
    line-height: 1;
    color: var(--gold);
    letter-spacing: 2px;
  }

  .person {
    position: absolute;
    left: 41px;
    top: 254px;
  }
  .person__name {
    font-size: 23px;
    font-weight: 700;
    color: var(--teal);
    letter-spacing: 0.3px;
    line-height: 1.2;
  }
  .person__role {
    font-size: 23px;
    color: var(--ink);
    line-height: 1.25;
  }
  .divider {
    position: absolute;
    left: 41px;
    top: 318px;
    width: 822px;
    height: 2px;
    background: var(--rule);
  }

  .contact {
    position: absolute;
    left: 452px;
    top: 368px;
    list-style: none;
  }
  .contact__item {
    display: flex;
    align-items: center;
    gap: 12px;
    font-size: 22px;
    color: var(--ink);
    height: 32.5px;
  }
  .contact__icon { width: 20px; height: 20px; flex: none; }

  .band {
    position: absolute;
    bottom: 0;
    height: 18px;
  }
  .band--teal { left: 0; width: 447px; background: var(--teal); }
  .band--gold { left: 452px; right: 0; background: var(--gold); }

  .back-art { display: block; width: 900px; height: 514px; }
  .headline { font-family: "Open Sans", Arial, sans-serif; font-weight: 700; fill: #fff; }
  .jargon {
    font-family: "Open Sans", Arial, sans-serif;
    font-stretch: 75%;
    font-variation-settings: "wdth" 75;
    font-weight: 400;
    font-size: 62px;
    fill: #fff;
  }
</style>
</head>
<body>

<section class="card card--front" aria-label="Business card front">
  <div class="brand">
    <span class="brand__mark"></span>
    <span class="brand__name">TRV</span>
  </div>

  <div class="person">
    <p class="person__name">DANIEL MARSH</p>
    <p class="person__role">Managing Director</p>
  </div>
  <div class="divider"></div>

  <ul class="contact">
    <li class="contact__item">
      <svg class="contact__icon" viewBox="0 0 20 20" aria-hidden="true">
        <path d="M4 3h4l1.5 4-2.2 1.5a11 11 0 0 0 4.2 4.2L13 10.5l4 1.5v4c0 1-1 2-2 2C8.5 18 2 11.5 2 5c0-1 1-2 2-2z" fill="var(--teal)"/>
      </svg>
      555-014-2276
    </li>
    <li class="contact__item">
      <svg class="contact__icon" viewBox="0 0 20 20" aria-hidden="true">
        <rect x="1" y="4" width="18" height="13" rx="1.5" fill="var(--teal)"/>
        <path d="M2 5.5l8 6 8-6" fill="none" stroke="#fff" stroke-width="1.6"/>
      </svg>
      dmarsh@tarvexa.studio
    </li>
    <li class="contact__item">
      <svg class="contact__icon" viewBox="0 0 20 20" aria-hidden="true">
        <circle cx="10" cy="10" r="8.5" fill="var(--teal)"/>
        <g fill="none" stroke="#fff" stroke-width="1.2">
          <ellipse cx="10" cy="10" rx="3.6" ry="8.5"/>
          <path d="M1.5 10h17M3 6h14M3 14h14"/>
        </g>
      </svg>
      www.tarvexa.studio
    </li>
  </ul>

  <div class="band band--teal"></div>
  <div class="band band--gold"></div>
</section>

<section class="card card--back" aria-label="Business card back">
  <svg class="back-art" viewBox="0 0 900 514" aria-labelledby="back-title">
    <title id="back-title">How can we help? List of services</title>
    <text class="headline" x="36" y="119" font-size="121" textLength="250" lengthAdjust="spacingAndGlyphs">HOW</text>
    <text class="headline" x="36" y="235" font-size="121" textLength="247" lengthAdjust="spacingAndGlyphs">CAN</text>
    <text class="headline" x="40" y="384" font-size="185" textLength="237" lengthAdjust="spacingAndGlyphs">WE</text>
    <text class="headline" x="33" y="476" font-size="105" textLength="268" lengthAdjust="spacingAndGlyphs">HELP?</text>

    <line x1="321" y1="28" x2="321" y2="476" stroke="#fff" stroke-width="2"/>

    <text class="jargon" x="360" y="75" textLength="461" lengthAdjust="spacingAndGlyphs">MOBILE LEARNING SCORM</text>
    <text class="jargon" x="360" y="156" textLength="510" lengthAdjust="spacingAndGlyphs">INSTRUCTIONAL DESIGN LMS</text>
    <text class="jargon" x="360" y="235" textLength="472" lengthAdjust="spacingAndGlyphs">MOOCS ELEARNING HTML5</text>
    <text class="jargon" x="360" y="315" textLength="451" lengthAdjust="spacingAndGlyphs">ADULT LEARNING THEORY</text>
    <text class="jargon" x="360" y="396" textLength="486" lengthAdjust="spacingAndGlyphs">GAMIFICATION CLASSROOM</text>
    <text class="jargon" x="360" y="476" textLength="446" lengthAdjust="spacingAndGlyphs">XAPI BLENDED LEARNING</text>
  </svg>
</section>

</body>
</html>
```